BLORK Business Card

Quellmont Dwelling Additions and Refits. I need a business card designed for this new high end renovation business. I would like the logo centered on the back side with the ABN (71 903 226 417) on the bottom right hand corner.

I would like the following information placed on the other side along with some customized pattern or design.

Percival Oakden
Director
Phone: 1300 418 957
Fax: (02) 9316 4471
Website: www.blorkbuilding.com.au
Email: p.oakden@blorkbuilding.com.au
PO Box 87,
Wendlecove NSW 2094

(FB Logo) BLORK - Quellmont Dwelling Additions and Refits

The final design should communicate professionalism and trust.

Back side background colour: white
Front side: Undecided

```html
<!DOCTYPE html>
<html lang="en">
<head>
<meta charset="utf-8">
<title>BLORK Business Card</title>
<link rel="stylesheet" href="https://fonts.googleapis.com/css2?family=Jost:wght@300;400&display=swap">
<style>
  :root {
    --stage: #4a5354;
    --card-white: #ffffff;
    --brand-blue: #1f4fd6;
    --blue-top: #2f7bff;
    --blue-bottom: #1a4bd0;
    --abn-blue: #3a9ee8;
    --dark-top: #2b2c2e;
    --dark-bottom: #0e0f10;
    --name-ink: #101214;
    --detail-grey: #8c8f93;
    --icon-blue: #2a62e6;
  }
  * { box-sizing: border-box; margin: 0; padding: 0; }
  html, body { width: 1200px; height: 741px; overflow: hidden; }
  body {
    background: var(--stage);
    font-family: "Jost", sans-serif;
    position: relative;
  }
  .card {
    position: absolute;
    left: 399px;
    width: 409px;
    height: 237px;
    overflow: hidden;
  }
  .card-logo-side { top: 89px; background: var(--card-white); }
  .card-info-side { top: 412px; background: linear-gradient(var(--dark-top), var(--dark-bottom)); }

  .wordmark {
    position: absolute;
    left: 0; right: 0;
    top: 90px;
    text-align: center;
    font-size: 30px;
    font-weight: 400;
    letter-spacing: 2px;
    color: var(--brand-blue);
  }
  .abn {
    position: absolute;
    right: 8px;
    bottom: 4px;
    font-size: 12.5px;
    font-weight: 400;
    letter-spacing: 0.6px;
    color: var(--abn-blue);
  }

  .header-band { position: absolute; left: 0; top: 0; width: 409px; height: 80px; }
  .holder-name {
    position: absolute;
    left: 14px; top: 28px;
    font-size: 19px;
    font-weight: 400;
    letter-spacing: 0.6px;
    color: var(--name-ink);
  }
  .holder-role {
    position: absolute;
    left: 91px; top: 51px;
    font-size: 16px;
    font-weight: 300;
    letter-spacing: 0.6px;
    color: var(--brand-blue);
  }
  .contact-list { position: absolute; left: 187px; top: 111px; list-style: none; }
  .contact-list li {
    display: flex; align-items: center;
    height: 18px;
    font-size: 10.5px;
    font-weight: 300;
    letter-spacing: 0.4px;
    color: var(--detail-grey);
  }
  .contact-list svg { width: 10px; height: 10px; margin-right: 15px; fill: var(--icon-blue); flex: none; }
  .social-line {
    position: absolute;
    left: 9px; top: 218px;
    display: flex; align-items: center;
    font-size: 12.5px;
    font-weight: 400;
    letter-spacing: 0.4px;
    color: var(--brand-blue);
  }
  .social-square { width: 15px; height: 15px; background: var(--brand-blue); margin-right: 7px; }
</style>
</head>
<body>
  <section class="card card-logo-side">
    <div class="wordmark">BLORK</div>
    <div class="abn">71 903 226 417</div>
  </section>

  <section class="card card-info-side">
    <svg class="header-band" viewBox="0 0 409 80" aria-hidden="true">
      <defs>
        <linearGradient id="bandBlue" x1="0" y1="0" x2="0" y2="1">
          <stop offset="0" stop-color="var(--blue-top)"/>
          <stop offset="1" stop-color="var(--blue-bottom)"/>
        </linearGradient>
      </defs>
      <path d="M0 0 H409 V73 Q205 30 0 75 Z" fill="url(#bandBlue)"/>
    </svg>
    <div class="holder-name">Percival Oakden</div>
    <div class="holder-role">Director</div>

    <ul class="contact-list">
      <li><svg viewBox="0 0 10 10"><path d="M2 0.5 L3.8 2.6 L2.9 3.7 Q4 6 6.3 7.1 L7.4 6.2 L9.5 8 L8.3 9.5 Q2 8.5 0.5 1.7 Z"/></svg>1300 418 957</li>
      <li><svg viewBox="0 0 10 10"><rect x="2.5" y="0.5" width="5" height="3"/><rect x="0.5" y="3.5" width="9" height="4" rx="1"/><rect x="2.5" y="6.5" width="5" height="3"/></svg>(02) 9316 4471</li>
      <li><svg viewBox="0 0 10 10"><circle cx="5" cy="5" r="4.5"/><path d="M0.5 5 H9.5 M5 0.5 V9.5" stroke="var(--dark-top)" stroke-width="0.8"/></svg>www.blorkbuilding.com.au</li>
      <li><svg viewBox="0 0 10 10"><rect x="0.5" y="2" width="9" height="6.5"/><path d="M0.5 2 L5 5.8 L9.5 2" fill="none" stroke="var(--dark-top)" stroke-width="0.8"/></svg>p.oakden@blorkbuilding.com.au</li>
      <li><svg viewBox="0 0 10 10"><path d="M5 0.5 L9.8 4.8 H8.5 V9.5 H6 V6.5 H4 V9.5 H1.5 V4.8 H0.2 Z"/></svg>PO Box 87, Wendlecove NSW 2094</li>
    </ul>

    <div class="social-line"><span class="social-square"></span>Quellmont Dwelling Additions and Refits</div>
  </section>
</body>
</html>
```